Clearpath Ledger Billing Company Business card

Need a business card that stands out that includes name of company,(above) Owners name Marisol Whitfield phone#555-314-7762 email# ClearpathLedgerBC@mailbox-example.com and website www.Clearpathledgerbillingcompany-example.com. This is a medical billing company so the card has to relate to that or relate to steady cashflow

```html
<!DOCTYPE html>
<html lang="en">
<head>
<meta charset="utf-8">
<title>Clearpath Ledger Billing Company – Business Card</title>
<link rel="stylesheet" href="https://fonts.googleapis.com/css2?family=PT+Sans:wght@400;700&display=swap">
<style>
  :root {
    --backdrop: #9b9b9b;
    --card-white: #f4f4f2;
    --navy: #0a3d8a;
    --navy-tint: rgba(255, 255, 255, 0.09);
    --green: #8cc63f;
    --ink-grey: #4f5256;
    --white: #ffffff;
  }
  * { box-sizing: border-box; margin: 0; padding: 0; }
  html, body {
    width: 1105px;
    height: 1200px;
    overflow: hidden;
    background: var(--backdrop);
    font-family: "PT Sans", Arial, sans-serif;
  }
  .canvas {
    position: relative;
    width: 1105px;
    height: 1200px;
  }
  .card {
    position: absolute;
    left: 182px;
    width: 747px;
    height: 427px;
    overflow: hidden;
  }
  .card--front { top: 119px; background: var(--card-white); }
  .card--back  { top: 637px; background: var(--navy); }

  /* Front */
  .brand {
    position: absolute;
    right: 44px;
    top: 118px;
    display: flex;
    align-items: center;
    gap: 14px;
  }
  .brand__mark {
    width: 26px;
    height: 26px;
    background: var(--green);
  }
  .brand__name {
    font-size: 24px;
    font-weight: 700;
    color: var(--navy);
    text-transform: uppercase;
    letter-spacing: 0.8px;
    line-height: 26px;
    text-align: center;
  }
  .holder {
    position: absolute;
    left: 43px;
    top: 248px;
  }
  .holder__name {
    font-size: 28px;
    font-weight: 700;
    color: var(--navy);
    line-height: 1;
  }
  .holder__role {
    margin-top: 8px;
    font-size: 19px;
    color: var(--green);
    line-height: 1;
  }
  .divider {
    position: absolute;
    left: 39px;
    right: 42px;
    top: 323px;
    height: 0;
    border-top: 1.5px solid var(--green);
  }
  .contact {
    position: absolute;
    left: 39px;
    top: 335px;
    font-size: 19px;
    color: var(--ink-grey);
    line-height: 28px;
  }
  .phone {
    position: absolute;
    right: 42px;
    top: 363px;
    font-size: 19px;
    color: var(--ink-grey);
    line-height: 28px;
  }
  .phone__label { color: var(--navy); font-weight: 700; }

  /* Back */
  .back__mark {
    position: absolute;
    left: 258px;
    top: 30px;
    width: 232px;
    height: 232px;
    background: var(--navy-tint);
  }
  .back__name {
    position: absolute;
    left: 0;
    right: 0;
    top: 278px;
    text-align: center;
    font-size: 26px;
    font-weight: 700;
    color: var(--white);
    text-transform: uppercase;
    letter-spacing: 1px;
    line-height: 27px;
  }
  .back__web {
    position: absolute;
    left: 0;
    right: 0;
    top: 336px;
    text-align: center;
    font-size: 21px;
    color: var(--white);
    line-height: 26px;
  }
</style>
</head>
<body>
<main class="canvas">
  <section class="card card--front" aria-label="Business card front">
    <div class="brand">
      <span class="brand__mark" aria-hidden="true"></span>
      <p class="brand__name">Clearpath Ledger<br>Billing Company</p>
    </div>
    <div class="holder">
      <p class="holder__name">Marisol Whitfield</p>
      <p class="holder__role">Owners</p>
    </div>
    <div class="divider"></div>
    <div class="contact">
      <p>ClearpathLedgerBC@mailbox-example.com</p>
      <p>Clearpathledgerbillingcompany-example.com</p>
    </div>
    <p class="phone"><span class="phone__label">P :</span> 555-314-7762</p>
  </section>

  <section class="card card--back" aria-label="Business card back">
    <span class="back__mark" aria-hidden="true"></span>
    <p class="back__name">Clearpath Ledger<br>Billing Company</p>
    <p class="back__web">Clearpathledgerbillingcompany-example.com</p>
  </section>
</main>
</body>
</html>
```